Business that Cleans the dishes and utensils used in private jets needs a flyer to describe its b...

I need a flyer to describe a HK based company called 'Vantor Rinsing'. We help the flight attendants to clean valuable dishes and utensils to save them time and costs. Color green is preferable. The design shall be easy to read and clear

Target Market(s)

Flight attendants and flight operations management

Industry/Entity Type

Aviation

Colors

Designer to choose colors to be used in the design.

Requirements
Must have
• Clean and professional.

```html
<!DOCTYPE html>
<html lang="en">
<head>
<meta charset="utf-8">
<title>Vantor Rinsing Flyer</title>
<link href="https://fonts.googleapis.com/css2?family=Oswald:wght@500;600;700&family=Montserrat:wght@400;500;600;700&display=swap" rel="stylesheet">
<style>
  :root{
    --green-dark:#0b4f2e;
    --green:#0f7a4a;
    --green-bright:#22b07a;
    --gold-dark:#b07d0c;
    --gold:#e0a91a;
    --gold-light:#f6d23a;
    --grey:#d9d9d9;
    --ink:#2b2b2b;
    --muted:#777;
    --bg:#eeeeea;
  }
  *{box-sizing:border-box;margin:0;padding:0}
  html,body{width:1200px;height:1200px;overflow:hidden;background:var(--bg)}
  .canvas{position:relative;width:1200px;height:1200px}
  .flyer{position:absolute;left:190px;top:20px;width:820px;height:1160px;background:#fff;overflow:hidden;box-shadow:0 6px 24px rgba(0,0,0,.15);font-family:"Montserrat",sans-serif}
  .flyer-art{position:absolute;inset:0}
  .headline{position:absolute;left:50px;top:130px;font-family:"Oswald",sans-serif;font-weight:700;font-size:118px;line-height:.98;letter-spacing:1px;text-transform:uppercase;background:linear-gradient(180deg,var(--green-bright),var(--green-dark));-webkit-background-clip:text;background-clip:text;color:transparent}
  .tagline{position:absolute;left:54px;top:400px;width:380px;font-size:18px;font-weight:600;line-height:1.3;color:var(--ink)}
  .pill{position:absolute;left:54px;top:490px;padding:9px 26px;border-radius:0 22px 22px 0;background:linear-gradient(90deg,var(--gold-dark),var(--gold-light));color:#fff;font-weight:700;font-size:19px;letter-spacing:1px}
  .features{position:absolute;left:40px;top:565px;display:flex;gap:12px;list-style:none}
  .feature{width:110px;text-align:center;color:var(--muted);font-size:14px;line-height:1.3}
  .feature svg{display:block;margin:0 auto 8px}
  .offer{position:absolute;left:600px;top:110px;width:190px;height:190px;border-radius:18px;background:linear-gradient(160deg,var(--gold-light),var(--gold-dark));color:#fff;font-family:"Oswald",sans-serif;font-weight:700;text-align:center;line-height:.9;padding-top:22px}
  .offer-amount{font-size:96px;display:block}
  .offer-label{font-size:56px;display:block}
  .benefits{position:absolute;left:60px;top:768px;width:290px;color:#fff}
  .benefits h2{font-size:22px;font-weight:700;line-height:1.05;margin-bottom:12px;text-transform:uppercase}
  .benefits ul{list-style:none}
  .benefits li{font-size:15px;line-height:1.25;margin-bottom:8px;padding-left:22px;position:relative}
  .benefits li::before{content:"";position:absolute;left:0;top:3px;width:12px;height:12px;border:2px solid #fff;border-radius:50%}
  .contact{position:absolute;left:240px;top:1050px;color:var(--ink)}
  .contact-label{font-size:22px;font-weight:700;letter-spacing:1px;color:#555;line-height:1.2}
  .contact-phone{font-family:"Oswald",sans-serif;font-size:52px;font-weight:700;line-height:1;color:var(--green)}
  .contact-lines{display:flex;gap:24px;font-size:14px;margin-top:6px;color:#444}
</style>
</head>
<body>
<div class="canvas">
  <section class="flyer">
    <svg class="flyer-art" width="820" height="1160" viewBox="0 0 820 1160">
      <defs>
        <linearGradient id="greenField" x1="0" y1="0" x2="0" y2="1">
          <stop offset="0" stop-color="#0b4f2e"/><stop offset="1" stop-color="#138a55"/>
        </linearGradient>
        <linearGradient id="goldField" x1="0" y1="0" x2="1" y2="1">
          <stop offset="0" stop-color="#f6d23a"/><stop offset="1" stop-color="#b07d0c"/>
        </linearGradient>
      </defs>
      <path class="swoosh" d="M300 60 Q580 20 820 80 L820 1010 L500 1010 C440 760 560 420 520 260 C495 160 420 100 300 60Z" fill="var(--grey)"/>
      <path class="green-field" d="M360 55 Q600 25 820 85 L820 990 L530 990 C480 740 600 420 560 250 C540 160 470 95 360 55Z" fill="url(#greenField)"/>
      <path d="M450 990 C520 1000 640 985 820 1000 L820 1160 L450 1160Z" fill="#fff"/>
      <rect x="500" y="300" width="300" height="680" rx="20" fill="#2f7a58" opacity=".85" role="img" aria-label="Photo of a cleaner in an apron wiping a surface with a sponge"/>
      <path class="gold-wave" d="M0 740 C120 670 300 700 430 660 L520 660 L540 1030 C380 1000 180 1060 0 1040Z" fill="url(#goldField)"/>
      <circle cx="560" cy="790" r="138" fill="#fff"/>
      <circle cx="560" cy="790" r="128" fill="#8aa6c4" role="img" aria-label="Photo of a smiling flight attendant in uniform"/>
      <circle cx="620" cy="980" r="108" fill="#fff"/>
      <circle cx="620" cy="980" r="98" fill="#b96b5a" role="img" aria-label="Photo of passengers seated in an aircraft cabin"/>
      <circle cx="730" cy="1075" r="80" fill="#fff"/>
      <circle cx="730" cy="1075" r="71" fill="#c9ccd1" role="img" aria-label="Photo of a cleaner in pink gloves wiping glass"/>
    </svg>

    <h1 class="headline">Vantor<br>Rinsing</h1>
    <p class="tagline">We help the flight attendants to clean valuable dishes and utensils to save them time and costs</p>
    <div class="pill">LOREM IMPSUM</div>

    <ul class="features">
      <li class="feature">
        <svg width="46" height="46" viewBox="0 0 46 46" fill="none" stroke="#999" stroke-width="2"><rect x="6" y="4" width="26" height="34" rx="3"/><circle cx="30" cy="30" r="9"/><path d="M10 12h14M10 18h10M38 6l2 4 4 2-4 2-2 4-2-4-4-2 4-2z"/></svg>
        Lorem ipsum dolor sit amet
      </li>
      <li class="feature">
        <svg width="46" height="46" viewBox="0 0 46 46" fill="none" stroke="#999" stroke-width="2"><rect x="6" y="4" width="26" height="34" rx="3"/><circle cx="30" cy="30" r="9"/><path d="M10 12h14M10 18h10M38 6l2 4 4 2-4 2-2 4-2-4-4-2 4-2z"/></svg>
        Lorem ipsum dolor sit amet
      </li>
      <li class="feature">
        <svg width="46" height="46" viewBox="0 0 46 46" fill="none" stroke="#999" stroke-width="2"><rect x="6" y="4" width="26" height="34" rx="3"/><circle cx="30" cy="30" r="9"/><path d="M10 12h14M10 18h10M38 6l2 4 4 2-4 2-2 4-2-4-4-2 4-2z"/></svg>
        Lorem ipsum dolor sit amet
      </li>
    </ul>

    <div class="offer"><span class="offer-amount">$50</span><span class="offer-label">OFF</span></div>

    <div class="benefits">
      <h2>Lorem<br>Impsum</h2>
      <ul>
        <li>Lorem ipsum dolor sit amet, consectetur.</li>
        <li>Lorem ipsum dolor sit amet, consectetur.</li>
        <li>Lorem ipsum dolor sit amet, consectetur.</li>
        <li>Lorem ipsum dolor sit amet, consectetur.</li>
      </ul>
    </div>

    <div class="contact">
      <div class="contact-label">CALL US</div>
      <div class="contact-phone">28104736</div>
      <div class="contact-lines"><span>hello@vantorrinsing.hk</span><span>www.vantorrinsing.hk</span></div>
    </div>
  </section>
</div>
</body>
</html>
```